KVB Business Card Design

We need a business card that emphasizes consulting services worldwide. The name of the company is KVB Consulting Group. We provide consulting services across several industries including but not limited to commodities, telecom, manufacturing, logistics, marketing and operations. We would like to see a creative design that emphasizes the global aspect, including Latin America and US markets, as well the bilingual nature of the service offerings.

The contact information section should include icons to represent the following data:
1) Name, Title and Company Name
2) Mobile Number
3) Skype ID
4) Email
5) Web Page
6) Location

We would like to see a card that emphasizes the worldwide concept. The back of the card should be simple, including only the logo (or a portion of the logo) and the slogan.

We would also like to see business cards in a booklet format. The colors to be used should be the same combination of colors used in the logos attached to this brief.

The logo design and some business card examples from Artvane Hub are attached for reference on style and look.

Target Market(s)

International business executives, 45-65 years of age, bilingual

Industry/Entity Type

Marketing

Colors
0792cd
34a7d8
85cae6
ffffff
cee9f5
ecf7fb

Requirements
Must have
• Please follow colors in logo attached.

2) Mobile Number
3) Skype ID
4) Email
5) Web Page
6) Location
Nice to have
• Global concept, consulting profile, diverse industry focus
Should not have
• No black color

```html
<!DOCTYPE html>
<html lang="en">
<head>
<meta charset="UTF-8">
<title>KVB Consulting Group – Business Card</title>
<link rel="stylesheet" href="https://fonts.googleapis.com/css2?family=Questrial&family=Didact+Gothic&display=swap">
<style>
  :root {
    --brand-deep: #0792cd;
    --brand-mid: #34a7d8;
    --brand-soft: #85cae6;
    --brand-pale: #cee9f5;
    --brand-mist: #ecf7fb;
    --paper: #ffffff;
    --ink-grey: #6f7a80;
    --ink-slate: #5a6a72;
    --backdrop: #e9edf0;
  }
  * { margin: 0; padding: 0; box-sizing: border-box; }
  html, body {
    width: 1200px; height: 900px; overflow: hidden;
    background: var(--backdrop);
  }
  .stage { position: relative; width: 1200px; height: 900px; }
  .card {
    position: absolute; left: 320px; width: 560px; height: 320px;
    box-shadow: 0 6px 18px rgba(60, 80, 95, 0.18);
    overflow: hidden;
    font-family: "Questrial", sans-serif;
  }

  /* Back of card */
  .card-back {
    top: 110px;
    background: linear-gradient(160deg, #e1f1f8 0%, var(--brand-pale) 55%, #c6e3f0 100%);
    display: flex; align-items: center; justify-content: center; gap: 16px;
  }
  .brand-square {
    width: 26px; height: 26px; background: var(--brand-soft); flex: none;
  }
  .brand-name {
    font-family: "Questrial", sans-serif; font-weight: 400;
    font-size: 40px; line-height: 1; letter-spacing: 2px;
    color: var(--brand-mid); text-transform: uppercase;
  }

  /* Front of card */
  .card-front { top: 470px; background: var(--paper); }
  .person { position: absolute; left: 200px; top: 50px; }
  .person-name {
    font-family: "Didact Gothic", sans-serif; font-weight: 400;
    font-size: 24px; color: var(--ink-slate); letter-spacing: 0.3px;
    -webkit-text-stroke: 0.5px var(--ink-slate);
  }
  .person-title { font-size: 14px; color: var(--brand-mid); margin-top: 2px; }

  .info-panel {
    position: absolute; left: 300px; right: 0; top: 128px; height: 128px;
    background: var(--brand-pale);
  }
  .contact-values {
    position: absolute; right: 275px; top: 140px;
    text-align: right; font-size: 13px; line-height: 22px; color: var(--ink-grey);
    white-space: nowrap;
  }
  .contact-labels {
    position: absolute; left: 316px; top: 140px;
    font-size: 13px; line-height: 22px; color: var(--brand-deep);
    letter-spacing: 0.5px; text-transform: uppercase;
  }
  .contact-row { display: flex; align-items: center; gap: 7px; height: 22px; }
  .contact-icon { width: 12px; height: 12px; flex: none; }
</style>
</head>
<body>
<main class="stage">

  <section class="card card-back" aria-label="Card back">
    <span class="brand-square"></span>
    <span class="brand-name">KVB Consulting Group</span>
  </section>

  <section class="card card-front" aria-label="Card front">
    <div class="person">
      <div class="person-name">Lucia Ferrer</div>
      <div class="person-title">Online Marketing Strategist</div>
    </div>

    <div class="info-panel"></div>

    <div class="contact-values">
      <div>+1 305 555-0148</div>
      <div>Brisa Key, FL</div>
      <div>lferrer@kvbmail.com</div>
      <div>kvbconsultgroup</div>
    </div>

    <div class="contact-labels">
      <div class="contact-row">
        <svg class="contact-icon" viewBox="0 0 12 12" aria-hidden="true">
          <rect x="3" y="0.5" width="6" height="11" rx="1.2" fill="none" stroke="var(--brand-deep)" stroke-width="1.2"/>
          <circle cx="6" cy="9.3" r="0.7" fill="var(--brand-deep)"/>
        </svg>
        <span>Mobile</span>
      </div>
      <div class="contact-row">
        <svg class="contact-icon" viewBox="0 0 12 12" aria-hidden="true">
          <path d="M6 11.5 C3 7.8 2 6.2 2 4.3 A4 4 0 0 1 10 4.3 C10 6.2 9 7.8 6 11.5 Z" fill="var(--brand-deep)"/>
          <circle cx="6" cy="4.3" r="1.4" fill="var(--brand-pale)"/>
        </svg>
        <span>Address</span>
      </div>
      <div class="contact-row">
        <svg class="contact-icon" viewBox="0 0 12 12" aria-hidden="true">
          <rect x="0.6" y="2.2" width="10.8" height="7.6" fill="none" stroke="var(--brand-deep)" stroke-width="1.2"/>
          <path d="M0.8 2.6 L6 6.6 L11.2 2.6" fill="none" stroke="var(--brand-deep)" stroke-width="1.2"/>
        </svg>
        <span>Email</span>
      </div>
      <div class="contact-row">
        <svg class="contact-icon" viewBox="0 0 12 12" aria-label="Chat ID">
          <circle cx="6" cy="6" r="6" fill="var(--brand-deep)"/>
        </svg>
      </div>
    </div>
  </section>

</main>
</body>
</html>
```